Granite Ridge Holdings

I have a real estate investment business.

** I need editable vector files of the final design.

Industry/Entity Type

Real Estate

Contact Information for Business Card

I would like the card to be clear and direct with the company name and contact info. I would prefer not to have a design that is too busy (i.e., with excessive detail) in the business card.

Font styles to use
Sans Serif

Requirements
Must have
• My card must have the following information listed below:
• Company name: Grainite Ridge Holdings LLC
• My name: Daniel Vorsley
• Phone number: (555) 218-9067
• Email address: dtvorsley@mailbox-example.net
• Keywords: “Real Estate Investments”
Nice to have
• I would like to have a design that resembles the characteristics/uses of obsidian stone which resembles something related to strength and resilience. Perhaps something with sharp, sleek color transitions as well.

```html
<!DOCTYPE html>
<html lang="en">
<head>
<meta charset="utf-8">
<title>Grainite Ridge Holdings LLC — Business Card</title>
<link href="https://fonts.googleapis.com/css2?family=Lato:ital,wght@0,400;0,700;1,400&display=swap" rel="stylesheet">
<style>
  :root {
    --brand-blue: #0015d6;
    --ink: #1c1c1c;
    --paper: #ffffff;
  }
  * { margin: 0; padding: 0; box-sizing: border-box; }
  html, body {
    width: 1200px;
    height: 800px;
    overflow: hidden;
    background: var(--paper);
  }
  .card {
    position: relative;
    width: 1200px;
    height: 800px;
    background: var(--paper);
    font-family: "Lato", sans-serif;
    color: var(--ink);
  }
  .company-band {
    position: absolute;
    left: 754px;
    top: 67px;
    width: 446px;
    height: 91px;
    background: var(--brand-blue);
    padding: 15px 0 0 39px;
  }
  .company-name {
    color: var(--paper);
    font-weight: 700;
    font-size: 22px;
    line-height: 28px;
    text-transform: uppercase;
  }
  .tagline {
    position: absolute;
    left: 793px;
    top: 178px;
    font-style: italic;
    font-size: 17px;
  }
  .holder-name {
    position: absolute;
    left: 155px;
    top: 394px;
    color: var(--brand-blue);
    font-weight: 700;
    font-size: 61px;
    line-height: 64px;
    letter-spacing: 0.08em;
    text-transform: uppercase;
  }
  .divider {
    position: absolute;
    left: 0;
    top: 561px;
    width: 1200px;
    height: 3px;
    background: var(--brand-blue);
  }
  .contact {
    position: absolute;
    left: 158px;
    top: 620px;
    list-style: none;
    font-size: 22px;
  }
  .contact-item { height: 45px; line-height: 28px; }
  .contact-label { color: var(--brand-blue); margin-right: 10px; }
</style>
</head>
<body>
  <main class="card">
    <div class="company-band">
      <p class="company-name">Grainite Ridge<br>Holdings LLC</p>
    </div>
    <p class="tagline">Real Estate Investments</p>

    <h1 class="holder-name">Daniel<br>Vorsley</h1>

    <div class="divider"></div>

    <ul class="contact">
      <li class="contact-item"><span class="contact-label">Phone:</span>(555) 218-9067</li>
      <li class="contact-item"><span class="contact-label">E-mail:</span>dtvorsley@mailbox-example.net</li>
    </ul>
  </main>
</body>
</html>
```